Domestic Services and Home Organisation Business Flyer

Font styles to use
Serif
Decorative
Script

Colors
b666a9
86cfc6
eaf2ce
b7a5cd
f3f1f8
e4daeb
d3a5cc
cee9f5

```html
<!DOCTYPE html>
<html lang="en">
<head>
<meta charset="utf-8">
<title>Tidy Nest Helper – Domestic Cleans &amp; Home Organisation</title>
<link href="https://fonts.googleapis.com/css2?family=Amaranth:wght@700&family=Kalam:wght@400;700&family=Nunito:wght@300;400&display=swap" rel="stylesheet">
<style>
  :root{
    --teal:#a3d9d1;
    --teal-deep:#86cfc6;
    --plum:#4b2c5e;
    --orchid:#b666a9;
    --lavender:#b7a5cd;
    --lilac:#e4daeb;
    --mist:#f3f1f8;
    --pink:#d3a5cc;
    --white:#ffffff;
    --ink:#3d2a4a;
  }
  *{margin:0;padding:0;box-sizing:border-box}
  html,body{width:850px;height:1200px;overflow:hidden;background:#fff}
  .flyer{position:relative;width:850px;height:1200px;overflow:hidden;background:var(--teal);font-family:'Nunito',sans-serif;color:var(--ink)}
  .backdrop{position:absolute;inset:0}
  .top-rule{position:absolute;top:0;left:0;width:850px;height:8px;background:var(--plum)}

  .mascot{position:absolute;left:20px;top:30px;width:390px;height:460px;border-radius:45% 45% 20% 20%;
    background:radial-gradient(circle at 45% 35%,#f6d3b8 0 22%,transparent 23%),linear-gradient(180deg,#c9e9e3 0%,#9ad6cc 60%,#86cfc6 100%);opacity:.85}

  .brand{position:absolute;right:50px;top:34px;text-align:right}
  .brand-name{font-family:'Kalam',cursive;font-weight:700;font-size:44px;color:var(--plum);line-height:1}
  .brand-tag{margin-top:14px;font-size:22px;line-height:28px;color:var(--plum);font-weight:400}

  .headline{position:absolute;right:55px;top:272px;text-align:right;font-family:'Amaranth',sans-serif;font-weight:700;font-size:48px;line-height:44px;color:var(--plum)}
  .headline-sub{position:absolute;right:55px;top:408px;font-family:'Kalam',cursive;font-size:35px;color:var(--ink)}

  .polaroid{position:absolute;background:#fff;padding:14px 14px 0;box-shadow:0 3px 8px rgba(60,40,80,.25)}
  .polaroid .photo{width:100%;height:200px}
  .polaroid .caption{font-family:'Kalam',cursive;font-weight:700;font-size:28px;color:var(--plum);padding:16px 10px 0;height:80px;white-space:nowrap}
  .p-cleans{left:30px;top:492px;width:272px;transform:rotate(3deg)}
  .p-cleans .photo{background:linear-gradient(135deg,#d7dde0,#b9c9b8 50%,#e7c16a)}
  .p-organise{left:305px;top:505px;width:278px;transform:rotate(-3deg);z-index:2}
  .p-organise .photo{background:linear-gradient(135deg,#f1ece6,#d8c3a5 50%,#e6a9c0)}
  .p-organise .caption{text-align:center;font-size:27px;padding:16px 0 0}
  .p-relax{left:560px;top:512px;width:262px;transform:rotate(4deg);z-index:1}
  .p-relax .photo{background:linear-gradient(135deg,#e8e2da,#a89c90 50%,#5e6e86)}
  .p-relax .caption{padding:16px 0 0 44px}

  .cta-pill{position:absolute;left:267px;top:822px;width:316px;height:48px;background:var(--orchid);color:#fff;font-family:'Amaranth',sans-serif;font-weight:700;font-size:24px;line-height:48px;text-align:center}

  .ring{position:absolute;border:2px solid #fff;border-radius:50%}
  .ring-broom{left:640px;top:825px;width:112px;height:112px}
  .ring-spray{left:312px;top:968px;width:116px;height:116px}

  .banner{position:absolute;background:var(--plum);color:#fff;font-family:'Kalam',cursive;font-size:28px;white-space:nowrap}
  .banner-why{left:0;top:910px;width:285px;height:57px;padding:10px 0 0 54px;clip-path:polygon(0 0,270px 0,285px 57px,0 57px)}
  .banner-contact{left:498px;top:965px;width:274px;height:70px;padding:16px 0 0 36px;clip-path:polygon(0 0,274px 0,274px 70px,8px 70px)}

  .reasons{position:absolute;left:54px;top:985px;list-style:none;font-size:23px;font-weight:300;color:var(--ink)}
  .reasons li{position:relative;padding-left:40px;line-height:28px;margin-bottom:11px}
  .reasons svg{position:absolute;left:0;top:3px;width:26px;height:24px;fill:var(--plum)}

  .contact{position:absolute;left:470px;top:1056px;width:340px;text-align:center;font-size:22px;font-weight:400;color:var(--ink);font-style:normal}
  .contact p{display:flex;align-items:center;justify-content:center;gap:10px;height:38px}
  .contact svg{fill:var(--plum)}
  .socials{display:flex;justify-content:center;gap:6px;margin-top:6px}
  .socials span{width:32px;height:32px;border-radius:50%;background:var(--plum)}
</style>
</head>
<body>
<main class="flyer">
  <svg class="backdrop" width="850" height="1200" viewBox="0 0 850 1200" aria-hidden="true">
    <path d="M0 260 Q380 185 850 200 L850 1200 L0 1200 Z" fill="#fff"/>
    <path d="M0 238 Q380 165 850 176 L850 202 Q380 188 0 264 Z" fill="var(--lavender)"/>
    <path d="M0 600 Q450 535 850 585 L850 960 Q560 900 300 900 Q120 892 0 880 Z" fill="var(--lilac)"/>
    <path d="M280 900 Q600 888 850 870 L850 975 Q600 925 280 900 Z" fill="var(--lavender)"/>
    <path d="M0 872 Q220 885 440 912 L400 1200 L0 1200 Z" fill="var(--teal)"/>
  </svg>
  <div class="top-rule"></div>

  <div class="mascot" role="img" aria-label="Illustration of a cheerful cleaner in an apron holding a feather duster and cloth"></div>

  <header class="brand">
    <h1 class="brand-name">Tidy Nest Helper</h1>
    <p class="brand-tag">Specialising in all Domestic<br>Cleans and Home Organisation</p>
  </header>

  <h2 class="headline">Isn’t it about<br>time you had<br>more time?</h2>
  <p class="headline-sub">Well I’m ready when you are!</p>

  <figure class="polaroid p-cleans">
    <div class="photo" role="img" aria-label="Photo of cleaning bottles and lemons in a caddy"></div>
    <figcaption class="caption">Domestic cleans</figcaption>
  </figure>
  <figure class="polaroid p-organise">
    <div class="photo" role="img" aria-label="Photo of neatly organised shelves with baskets and files"></div>
    <figcaption class="caption">Home organisation</figcaption>
  </figure>
  <figure class="polaroid p-relax">
    <div class="photo" role="img" aria-label="Photo of someone relaxing with a cup of tea"></div>
    <figcaption class="caption">Hassle-free</figcaption>
  </figure>

  <div class="cta-pill">Get back some ‘me’ time!</div>

  <div class="ring ring-broom"></div>
  <div class="ring ring-spray"></div>

  <div class="banner banner-why">Why choose me?</div>
  <ul class="reasons">
    <li><svg viewBox="0 0 24 23"><path d="M12 0l3.1 7.6 8.2.6-6.3 5.3 2 8L12 17.2 4.9 21.5l2-8L.7 8.2l8.2-.6z"/></svg>experienced</li>
    <li><svg viewBox="0 0 24 23"><path d="M12 0l3.1 7.6 8.2.6-6.3 5.3 2 8L12 17.2 4.9 21.5l2-8L.7 8.2l8.2-.6z"/></svg>fully insured</li>
    <li><svg viewBox="0 0 24 23"><path d="M12 0l3.1 7.6 8.2.6-6.3 5.3 2 8L12 17.2 4.9 21.5l2-8L.7 8.2l8.2-.6z"/></svg>trustworthy &amp; reliable</li>
    <li><svg viewBox="0 0 24 23"><path d="M12 0l3.1 7.6 8.2.6-6.3 5.3 2 8L12 17.2 4.9 21.5l2-8L.7 8.2l8.2-.6z"/></svg>committed to making<br>your life hassle-free!</li>
  </ul>

  <div class="banner banner-contact">Get in touch today</div>
  <address class="contact">
    <p><svg width="28" height="20" viewBox="0 0 28 20"><path d="M0 0h28v20H0z M2 2v.6l12 9 12-9V2z M2 5v13h24V5l-12 9z" fill-rule="evenodd"/></svg>hello@tidynesthelper.co.uk</p>
    <p><svg width="22" height="24" viewBox="0 0 22 24"><path d="M5 1l4 5-2.5 3c1.5 3.5 4 6 7.5 7.5l3-2.5 4 4-3 4C8 21 1 12 1 4z"/></svg>07700 900 418</p>
    <div class="socials"><span></span><span></span></div>
  </address>
</main>
</body>
</html>
```